Business Card with PUNCH
bluepinelodge.net
Project: Business Card with PUNCH
Business Card with PUNCH - Consulting
Creative Brief
Simple
Morris Trulsow
President
418 Dunmere Lane Suite 207 Spring, TX 77291
morris@bluepinelodge.net
logo on the back please
mtrulsow mtrulsow
WOW, what a tremendous effort overnight! Here is what I can tell you from what we have seen so far: 1. Prefer horizontal orientation of card rather than vertical. 2. Prefer the white cards with the blue and gray logo vs. the darker colors 3. Would like the back of the card to be white with room for a hand written note 4. Clear plastic cards are not a hit 5. Not a fan of card that look like the data is presented on any kind of a 'tab' or website type icons. Thanks for the many creative ideas, we are excited about this contest. mt

```html
<!DOCTYPE html>
<html lang="en">
<head>
<meta charset="utf-8">
<title>Business Card – Blue Pine Lodge</title>
<link href="https://fonts.googleapis.com/css2?family=Open+Sans:wght@400;600;700&display=swap" rel="stylesheet">
<style>
  :root {
    --backdrop: #e4e5e8;
    --card: #ffffff;
    --brand-blue: #2a2f8f;
    --rule-gray: #6d6f74;
    --ink: #3b3d42;
    --on-blue: #ffffff;
  }
  html, body {
    margin: 0;
    width: 1200px;
    height: 816px;
    overflow: hidden;
    background: var(--backdrop);
    font-family: "Open Sans", Arial, sans-serif;
  }
  .card {
    position: absolute;
    left: 70px;
    top: 105px;
    width: 1060px;
    height: 606px;
    background: var(--card);
    border-radius: 40px;
    overflow: hidden;
    box-shadow: 0 4px 18px rgba(0,0,0,0.12);
  }
  .brand {
    position: absolute;
    left: 56px;
    top: 212px;
    display: flex;
    align-items: center;
    gap: 12px;
  }
  .brand-dot {
    width: 34px;
    height: 34px;
    border-radius: 50%;
    background: var(--brand-blue);
  }
  .brand-name {
    font-size: 46px;
    font-weight: 700;
    color: var(--brand-blue);
    letter-spacing: -0.5px;
    line-height: 1;
  }
  .divider {
    position: absolute;
    left: 520px;
    right: 0;
    top: 250px;
    height: 2px;
    background: var(--rule-gray);
  }
  .name-band {
    position: absolute;
    left: 0;
    top: 290px;
    width: 420px;
    height: 92px;
    background: var(--brand-blue);
    border-radius: 0 46px 46px 0;
    color: var(--on-blue);
    text-align: right;
    box-sizing: border-box;
    padding: 14px 42px 0 0;
  }
  .person-name {
    font-size: 30px;
    font-weight: 600;
    line-height: 1.2;
  }
  .person-title {
    font-size: 19px;
    font-weight: 600;
    letter-spacing: 1px;
    text-transform: uppercase;
    margin-top: 2px;
  }
  .contacts {
    position: absolute;
    left: 64px;
    top: 432px;
    margin: 0;
    padding: 0;
    list-style: none;
    color: var(--ink);
    font-size: 19px;
  }
  .contacts li {
    display: flex;
    align-items: center;
    gap: 18px;
    height: 40px;
  }
  .contacts svg, .address svg { flex: none; fill: var(--brand-blue); }
  .address {
    position: absolute;
    right: 56px;
    top: 300px;
    display: flex;
    align-items: flex-start;
    gap: 14px;
    color: var(--ink);
    font-size: 19px;
    line-height: 1.4;
    text-align: right;
  }
  .address svg { margin-top: 4px; }
</style>
</head>
<body>
  <div class="card">
    <div class="brand">
      <span class="brand-dot"></span>
      <span class="brand-name">bluepinelodge.net</span>
    </div>
    <div class="divider"></div>

    <div class="name-band">
      <div class="person-name">Warren Calloway</div>
      <div class="person-title">General Manager</div>
    </div>

    <div class="address">
      <svg width="20" height="18" viewBox="0 0 20 18" aria-hidden="true">
        <path d="M10 0 L20 9 H17 V18 H12 V12 H8 V18 H3 V9 H0 Z"/>
      </svg>
      <div>418 Dunmere Lane Suite 207,<br>Spring TX, USA</div>
    </div>

    <ul class="contacts">
      <li>
        <svg width="18" height="18" viewBox="0 0 24 24" aria-hidden="true">
          <path d="M6.6 10.8a15.1 15.1 0 0 0 6.6 6.6l2.2-2.2c.3-.3.7-.4 1-.2 1.1.4 2.3.6 3.6.6.6 0 1 .4 1 1V20c0 .6-.4 1-1 1C10.6 21 3 13.4 3 4c0-.6.4-1 1-1h3.5c.6 0 1 .4 1 1 0 1.3.2 2.5.6 3.6.1.3 0 .7-.2 1z"/>
        </svg>
        <span>+2 (0114) 58-716-40</span>
      </li>
      <li>
        <svg width="18" height="14" viewBox="0 0 18 14" aria-hidden="true">
          <path d="M0 0 H18 V2 L9 8 L0 2 Z M0 4 L9 10 L18 4 V14 H0 Z"/>
        </svg>
        <span>info@bluepinelodge.net</span>
      </li>
      <li>
        <svg width="18" height="18" viewBox="0 0 18 18" aria-hidden="true">
          <circle cx="9" cy="9" r="8" fill="none" stroke="#2a2f8f" stroke-width="2"/>
          <ellipse cx="9" cy="9" rx="3.5" ry="8" fill="none" stroke="#2a2f8f" stroke-width="1.6"/>
          <rect x="1" y="8.2" width="16" height="1.6"/>
        </svg>
        <span>www.bluepinelodge.net</span>
      </li>
    </ul>
  </div>
</body>
</html>
```